Business card based on your logo design "Brennock&Co"

Can you please design a business card based on the logo artwork you designed for our business. Double sided as per your submitted image of possible application of logo.

```html
<!DOCTYPE html>
<html lang="en">
<head>
<meta charset="utf-8">
<title>Brennock&amp;Co — Business Card</title>
<link rel="stylesheet" href="https://fonts.googleapis.com/css2?family=Oswald:wght@600&family=Roboto:wght@400;500;700&display=swap">
<style>
  :root {
    --bg: #ececec;
    --card-white: #ffffff;
    --card-grey: #ebebeb;
    --ink: #1e1b1a;
    --ink-soft: #3a3a3a;
    --orange: #e0861b;
    --white: #ffffff;
  }
  * { margin: 0; padding: 0; box-sizing: border-box; }
  html, body {
    width: 1200px; height: 1001px; overflow: hidden;
    background: var(--bg);
    font-family: "Roboto", Arial, sans-serif;
  }
  .sheet {
    position: relative; width: 1200px; height: 1001px;
    display: flex; align-items: center; justify-content: center; gap: 60px;
  }
  .card {
    position: relative; width: 520px; height: 297px; overflow: hidden;
    box-shadow: 0 6px 18px rgba(0,0,0,0.12);
  }

  /* Front side */
  .card-front { background: var(--card-grey); }
  .front-band {
    position: absolute; left: 0; top: 0; width: 100%; height: 100%;
  }
  .front-logo {
    position: absolute; top: 22px; right: 34px;
    display: flex; align-items: center; gap: 10px;
  }
  .wordmark {
    font-family: "Oswald", Impact, sans-serif; font-weight: 600;
    letter-spacing: 1px; text-transform: uppercase; line-height: 1;
  }
  .front-logo .wordmark { color: var(--white); font-size: 34px; }
  .logo-square { width: 14px; height: 14px; background: var(--orange); }
  .front-stripe {
    position: absolute; left: 0; bottom: 34px; width: 100%; height: 9px;
    background: var(--ink);
  }
  .identity { position: absolute; left: 30px; top: 118px; }
  .identity .name { color: var(--orange); font-weight: 700; font-size: 19px; }
  .identity .role { color: var(--ink-soft); font-weight: 500; font-size: 16px; margin-top: 3px; }
  .contacts {
    position: absolute; left: 250px; top: 124px; list-style: none;
  }
  .contacts li {
    display: flex; align-items: center; gap: 9px;
    color: var(--ink); font-size: 13px; font-weight: 500; line-height: 22px;
  }
  .contacts svg { width: 13px; height: 13px; flex: none; fill: var(--orange); }

  /* Back side */
  .card-back {
    background: var(--card-white);
    display: flex; align-items: center; justify-content: center; gap: 14px;
  }
  .card-back .wordmark { color: var(--ink); font-size: 58px; }
  .card-back .logo-square { width: 22px; height: 22px; }
</style>
</head>
<body>
<main class="sheet">
  <section class="card card-front" aria-label="Business card front">
    <svg class="front-band" viewBox="0 0 520 297" preserveAspectRatio="none" aria-hidden="true">
      <polygon points="0,0 520,0 520,125 505,125 497,134 489,125 420,125 420,84 0,84" fill="#1e1b1a"/>
    </svg>
    <div class="front-logo">
      <span class="logo-square"></span>
      <span class="wordmark">Brennock&amp;Co</span>
    </div>
    <div class="identity">
      <p class="name">Your Name</p>
      <p class="role">Owner and CEO</p>
    </div>
    <ul class="contacts">
      <li>
        <svg viewBox="0 0 24 24"><path d="M12 2a7 7 0 0 0-7 7c0 5 7 13 7 13s7-8 7-13a7 7 0 0 0-7-7zm0 9.5A2.5 2.5 0 1 1 12 6.5a2.5 2.5 0 0 1 0 5z"/></svg>
        Your long address commercial or domestic
      </li>
      <li>
        <svg viewBox="0 0 24 24"><path d="M6.6 10.8a15 15 0 0 0 6.6 6.6l2.2-2.2a1 1 0 0 1 1-.25 11.4 11.4 0 0 0 3.6.57 1 1 0 0 1 1 1V20a1 1 0 0 1-1 1A17 17 0 0 1 3 4a1 1 0 0 1 1-1h3.5a1 1 0 0 1 1 1c0 1.25.2 2.45.57 3.6a1 1 0 0 1-.25 1z"/></svg>
        0000.1122.3344
      </li>
      <li>
        <svg viewBox="0 0 24 24"><path d="M2 5h20v14H2zm2 2v.5l8 5 8-5V7l-8 5z"/></svg>
        yourname@yourwebsite.com
      </li>
      <li>
        <svg viewBox="0 0 24 24"><path d="M12 2a10 10 0 1 0 0 20 10 10 0 0 0 0-20zm6.9 9h-3a15 15 0 0 0-1.4-6A8 8 0 0 1 18.9 11zM12 4c.9 1.2 1.8 3.6 2 7h-4c.2-3.4 1.1-5.8 2-7zM9.5 5A15 15 0 0 0 8.1 11h-3A8 8 0 0 1 9.5 5zM5.1 13h3a15 15 0 0 0 1.4 6A8 8 0 0 1 5.1 13zM12 20c-.9-1.2-1.8-3.6-2-7h4c-.2 3.4-1.1 5.8-2 7zm2.5-1a15 15 0 0 0 1.4-6h3a8 8 0 0 1-4.4 6z"/></svg>
        www.yourwebsite.com
      </li>
    </ul>
    <div class="front-stripe"></div>
  </section>

  <section class="card card-back" aria-label="Business card back">
    <span class="logo-square"></span>
    <span class="wordmark">Brennock&amp;Co</span>
  </section>
</main>
</body>
</html>
```